MOSLEN Environmental needs an upgrade to its current business cards design

We need an upgrade to our current business cards design, where the MOSLEN acronym is included, as possible and not being overloaded.
MOSLEN Environmental is an Environmental Consultancy Firm based in Sydney.
We would like to see creative designs different from the standard type of business cards (for example, rounded edges, different to standard size of common business cards.

Target Market(s)

industrial companies (oil & gas, petrochemical, mining, insolvency, finance and manufacturing), developers, architect firms, law firms.

Industry/Entity Type

Business

Contact Information for Business Card

logos (brand and acronym), if they don't appear overloaded.
name
role
name of company (MOSLEN Environmental),
address (Level 3, Suite 3C, 47-49 Dorrigan Lane, Wexmoor, NSW, 2188) landline (02 7314 2986)
mobile (staff member)
email (staff member) and
website (www.moslengreen.example).
Include: Contaminated Land, Site Remediation, Groundwater Assessment, Health and Ecological Risk Assessments, Acid Sulfate Soils, Waste Classification.

Font styles to use
Serif
Sans Serif

Requirements
Must have
• A creative design different to the standard type of business cards.
Nice to have
• Rounded edges
• Different size of business cards rather than the standard size.
Should not have
• Preferable not to use white colour background, unless it is required from a creative design proposed.
• Not an overloaded design.
• Avoid black colours

```html
<!DOCTYPE html>
<html lang="en">
<head>
<meta charset="utf-8">
<title>MOSLEN Environmental – Business Card</title>
<link rel="stylesheet" href="https://fonts.googleapis.com/css2?family=Open+Sans:wght@400;600;700&display=swap">
<style>
  :root {
    --stage: #6b6e72;
    --card: #2c2f33;
    --card-light: #363a3f;
    --green: #8cc63f;
    --green-dark: #6fa52a;
    --text: #f2f2f2;
    --muted: #b9bcc0;
    --rule: #5a5e63;
  }
  * { box-sizing: border-box; margin: 0; padding: 0; }
  html, body {
    width: 1200px; height: 950px; overflow: hidden;
    background: var(--stage);
    font-family: "Open Sans", Arial, sans-serif;
  }
  .canvas {
    position: relative; width: 1200px; height: 950px;
    display: flex; flex-direction: column; align-items: center; justify-content: center; gap: 50px;
  }
  .card {
    position: relative; width: 720px; height: 410px;
    background: linear-gradient(135deg, var(--card-light), var(--card));
    border-radius: 14px; overflow: hidden;
    box-shadow: 0 12px 30px rgba(0,0,0,.35);
  }
  .brand {
    position: absolute; display: flex; align-items: center; gap: 12px;
    color: var(--green); font-weight: 700; line-height: 1; white-space: nowrap;
  }
  .brand-mark { flex: none; border-radius: 50%; background: var(--green); }

  /* back */
  .card-back .brand { left: 150px; top: 150px; font-size: 38px; }
  .card-back .brand-mark { width: 18px; height: 18px; }
  .services {
    position: absolute; left: 150px; top: 230px; width: 440px;
    color: var(--muted); font-size: 15px; line-height: 1.6;
  }
  .services .dot { color: var(--green); margin: 0 6px; }

  /* front */
  .card-front .brand { left: 40px; top: 160px; font-size: 26px; gap: 10px; }
  .card-front .brand-mark { width: 14px; height: 14px; }
  .divider {
    position: absolute; left: 392px; top: 40px; width: 1px; height: 270px;
    background: var(--rule);
  }
  .contact { position: absolute; left: 420px; top: 44px; color: var(--text); font-size: 16px; line-height: 1.4; }
  .contact .person { color: var(--green); font-size: 24px; font-weight: 600; text-transform: uppercase; }
  .contact .role { font-size: 16px; text-transform: uppercase; letter-spacing: 1px; margin-bottom: 12px; }
  .contact .company { font-weight: 700; }
  .contact .address { margin-bottom: 10px; }
  .lines { list-style: none; }
  .lines li { display: flex; align-items: center; gap: 10px; margin-bottom: 3px; }
  .lines svg { width: 16px; height: 16px; flex: none; }
  .band {
    position: absolute; left: 0; right: 0; bottom: 0; height: 30px;
    background: linear-gradient(180deg, var(--green), var(--green-dark));
    border-top: 3px solid #45494e;
  }
</style>
</head>
<body>
<main class="canvas">
  <section class="card card-back">
    <div class="brand"><span class="brand-mark"></span>MOSLEN Environmental</div>
    <p class="services">
      Contaminated Land<span class="dot">•</span>Site Remediation<span class="dot">•</span>Groundwater Assessment<span class="dot">•</span>Health &amp; Ecological Risk Assessments<span class="dot">•</span>Acid Sulfate Soils<span class="dot">•</span>Waste Classification.
    </p>
  </section>

  <section class="card card-front">
    <div class="brand"><span class="brand-mark"></span>MOSLEN Environmental</div>
    <div class="divider"></div>
    <div class="contact">
      <p class="person">Alan Perry</p>
      <p class="role">President</p>
      <p class="company">MOSLEN Environmental</p>
      <p class="address">Level 3, Suite 3C<br>47-49 Dorrigan Lane<br>Wexmoor, NSW, 2188</p>
      <ul class="lines">
        <li><svg viewBox="0 0 16 16"><path fill="#8cc63f" d="M4 1l2.5 3-1.5 2c1 2 3 4 5 5l2-1.5 3 2.5-1.5 2.5C8 15 1 8 1.5 2.5z"/></svg>02 7314 2986</li>
        <li><svg viewBox="0 0 16 16"><rect x="4" y="1" width="8" height="14" rx="1.5" fill="#8cc63f"/><rect x="5.5" y="3" width="5" height="8" fill="#2c2f33"/></svg>0412 587 203</li>
        <li><svg viewBox="0 0 16 16"><rect x="1" y="3" width="14" height="10" rx="1" fill="#8cc63f"/><path d="M1.5 3.5L8 9l6.5-5.5" stroke="#2c2f33" stroke-width="1.3" fill="none"/></svg>name@moslengreen.example</li>
        <li><svg viewBox="0 0 16 16"><circle cx="8" cy="8" r="7" fill="#8cc63f"/><path d="M1 8h14M8 1c-3 3-3 11 0 14M8 1c3 3 3 11 0 14" stroke="#2c2f33" stroke-width="1" fill="none"/></svg>www.moslengreen.example</li>
      </ul>
    </div>
    <div class="band"></div>
  </section>
</main>
</body>
</html>
```